The Restful Airway & Jaw Clinic of Larchmont
Corinne T. Valdez D.D.S., Pharm.D, LVIF
The Restful Airway & Jaw Clinic of Larchmont - Health
Creative Brief
Use specific fonts
Use what works the best in your design
Professional
The Restful Airway & Jaw Clinic of LM
37 Gorse Lane Fenwick, OR 97431
cvaldezdds@quillmail.net
I like colors in Greens and complimentary colors. I prefers logos that are more abstract in design with elegant (not cursive) fonts. I am drawn to logos which look like abstract "faces" or "symbols". I treat many patients who are in pain, and would like my logo and design to exude a sense of well-being and serenity. I would like the logo to focus more on the "sleep" aspect (perhaps an abstract of a person sleeping?). Please no teeth or dental symbols! Please use several complimentary colors in the design. You may abbreviate "Larchmont" to "LM" if it works better in your design

```html
<!DOCTYPE html>
<html lang="en">
<head>
<meta charset="utf-8">
<title>The Restful Airway &amp; Jaw Clinic of LM – Business Cards</title>
<link rel="stylesheet" href="https://fonts.googleapis.com/css2?family=Arimo:wght@400;700&display=swap">
<style>
  :root {
    --green: #5cbc2a;
    --green-light: #8fd63a;
    --green-dark: #1f8f33;
    --ink: #1c1c1c;
    --border: #b9b9b9;
    --sheet: #ffffff;
  }
  * { margin: 0; padding: 0; box-sizing: border-box; }
  html, body { width: 1200px; height: 756px; overflow: hidden; background: var(--sheet); }
  body { position: relative; font-family: "Arimo", Arial, sans-serif; color: var(--ink); }

  .card {
    position: absolute;
    width: 545px; height: 348px;
    border-radius: 16px;
    overflow: hidden;
  }
  .card--front { background: #fff; border: 1.5px solid var(--border); }
  .card--back {
    background: radial-gradient(ellipse at 50% 50%, var(--green-light) 0%, var(--green) 55%, #45a820 100%);
  }
  .pos-tl { left: 29px; top: 12px; }
  .pos-tr { left: 605px; top: 12px; }
  .pos-bl { left: 29px; top: 384px; }
  .pos-br { left: 605px; top: 384px; }

  .brand { position: absolute; display: flex; align-items: center; gap: 14px; }
  .brand__dot { width: 40px; height: 40px; border-radius: 50%; background: var(--green); flex: none; }
  .brand__name { font-weight: 700; font-size: 19px; line-height: 1.2; color: var(--ink); }
  .brand--light .brand__dot { background: #fff; }
  .brand--light .brand__name { color: #fff; }
  .brand--deep .brand__dot { background: var(--green-dark); }
  .brand--deep .brand__name { color: var(--green-dark); }

  .holder { position: absolute; font-size: 12.5px; line-height: 1.35; }
  .contact { position: absolute; font-size: 12px; line-height: 1.38; }
  .contact b { display: inline-block; width: 22px; font-weight: 700; }

  .stripe { position: absolute; }
</style>
</head>
<body>

  <!-- Front, layout A -->
  <section class="card card--front pos-tl">
    <p class="holder" style="right:26px; top:8px;">Corinne T. Valdez D.D.S.<br>Pharm.D, LVIF</p>
    <div class="brand" style="left:178px; top:118px;">
      <span class="brand__dot"></span>
      <p class="brand__name">The Restful Airway<br>&amp; Jaw Clinic of LM</p>
    </div>
    <div class="stripe" style="left:0; top:236px; width:5px; height:110px; background:var(--green-dark);"></div>
    <div class="stripe" style="left:6px; top:236px; width:5px; height:110px; background:var(--green);"></div>
    <div class="contact" style="left:30px; top:238px;">
      37 Gorse Lane<br>Fenwick, OR 97431<br>
      <b>P :</b>541-555-0148<br>
      <b>F :</b>541-555-0192<br>
      <b>E :</b>cvaldezdds@quillmail.net
    </div>
  </section>

  <!-- Back, light mark -->
  <section class="card card--back pos-tr">
    <div class="brand brand--light" style="left:148px; top:150px;">
      <span class="brand__dot"></span>
      <p class="brand__name">The Restful Airway<br>&amp; Jaw Clinic of LM</p>
    </div>
  </section>

  <!-- Front, layout B -->
  <section class="card card--front pos-bl">
    <div class="stripe" style="left:0; top:24px; width:10px; height:300px; background:var(--green);"></div>
    <div class="stripe" style="left:12px; top:24px; width:4px; height:300px; background:var(--green-dark);"></div>
    <div class="stripe" style="right:12px; top:24px; width:4px; height:300px; background:var(--green-dark);"></div>
    <div class="stripe" style="right:0; top:24px; width:10px; height:300px; background:var(--green);"></div>
    <div class="brand" style="left:100px; top:70px;">
      <span class="brand__dot"></span>
      <p class="brand__name">The Restful Airway<br>&amp; Jaw Clinic of LM</p>
    </div>
    <p class="holder" style="left:120px; top:168px; font-size:13.5px;">Corinne T. Valdez D.D.S. Pharm.D, LVIF</p>
    <div class="contact" style="left:330px; top:222px;">
      37 Gorse Lane<br>Fenwick, OR 97431<br>
      <b>P :</b>541-555-0148<br>
      <b>F :</b>541-555-0192<br>
      <b>E :</b>cvaldezdds@quillmail.net
    </div>
  </section>

  <!-- Back, deep mark -->
  <section class="card card--back pos-br">
    <div class="brand brand--deep" style="left:150px; top:140px;">
      <span class="brand__dot"></span>
      <p class="brand__name">The Restful Airway<br>&amp; Jaw Clinic of LM</p>
    </div>
  </section>

</body>
</html>
```